In need of a fabulous a newsletter template!

We would like a Newsletter template designed for our practice that we can use on a quarterly basis to send out to our patients via email. This template should also be printable so we may have it printed for our waiting area and use for mailings. We envision a single page, double-sided. We would like to be able to fill out the template with out own material, but have a consistent layout with the following sections: 1) Patient Spotlight, 2) Upcoming Events, 3) Technology Update, 4) Pediatric Corner, 5) Exciting news, 6) Learn to Listen, 7) A note from Dr. Farrow. To view more about our company, visit our website at www.pinecrestaudio.example

Target Market(s)

Our patients --- Adults age 35-90

Industry/Entity Type

Healthcare

Font styles to use
Serif
Sans Serif

Colors
0892cd
34a7d8
0355a3
3377b5
85cae6

Requirements
Must have
• Eye-catching, organized, easy-to-follow layout so that we may send out information to our patients on a quarterly basis. Once created, we need to be able to fill in the information for the sections listed above. Must list our address and contact information on the front and back; probably in the header on the front and footer on the back.
Nice to have
• Sections 1-5 are needed from above, but would like to fit in sections 6-7, if available.

```html
<!DOCTYPE html>
<html lang="en">
<head>
<meta charset="utf-8">
<title>Pinecrest Audiology – Quarterly Newsletter</title>
<link href="https://fonts.googleapis.com/css2?family=Montserrat:wght@600;700&family=Open+Sans:wght@400;600;700&family=Playfair+Display:ital,wght@1,700&display=swap" rel="stylesheet">
<style>
  :root{
    --blue-deep:#0355a3;
    --blue:#0892cd;
    --blue-mid:#3377b5;
    --blue-light:#34a7d8;
    --sky:#85cae6;
    --sky-wash:#e5f4fb;
    --page:#e8e9eb;
    --card:#ffffff;
    --ink:#4a4f55;
    --ink-soft:#7a8088;
    --link:#d9344a;
    --rule:#d8dde2;
  }
  *{box-sizing:border-box;margin:0;padding:0}
  html,body{width:1200px;height:4000px;overflow:hidden}
  body{background:var(--page);font-family:"Open Sans",Arial,sans-serif;color:var(--ink);font-size:15px;line-height:1.5}
  .preheader{height:208px;padding-top:104px;text-align:center;font-size:15px;color:var(--ink-soft)}
  .preheader a{color:var(--link);text-decoration:underline}
  .newsletter{width:744px;height:3672px;margin:0 auto;background:var(--card);border-radius:14px;overflow:hidden}
  .newsletter > *{overflow:hidden}
  .section-title{font-family:Montserrat,Arial,sans-serif;font-weight:700;font-size:20px;line-height:28px;color:var(--blue-deep);text-align:center;text-transform:uppercase;letter-spacing:.5px}
  .btn{display:inline-block;background:var(--blue-deep);color:#fff;font-weight:600;font-size:14px;padding:12px 26px;border-radius:3px;text-decoration:none}
  .btn-outline{display:inline-block;border:1px solid var(--rule);color:var(--ink);font-size:13px;padding:7px 16px;border-radius:3px;background:#fff}

  .masthead{height:128px;display:flex;align-items:center;justify-content:space-between;padding:0 36px}
  .brand{display:flex;align-items:center;gap:12px;font-family:Montserrat,Arial,sans-serif;font-weight:700;font-size:21px;color:var(--blue-deep);text-transform:uppercase;letter-spacing:.5px}
  .brand-dot{width:28px;height:28px;border-radius:50%;background:var(--blue)}
  .masthead-phone{display:flex;align-items:center;gap:10px;font-size:15px}
  .icon-circle{flex:none;width:30px;height:30px;border-radius:50%;background:var(--blue);display:flex;align-items:center;justify-content:center}

  .hero{position:relative;height:336px;margin:0 36px;background:linear-gradient(180deg,#a9c9e2 0%,#8b6a58 40%,#6b4536 100%)}
  .hero-panel{position:absolute;left:0;top:112px;width:356px;height:144px;padding:22px 28px;background:rgba(3,85,163,.9)}
  .hero-panel h1{font-family:"Playfair Display",Georgia,serif;font-style:italic;font-weight:700;font-size:28px;color:#fff;line-height:1.2;margin-bottom:18px;white-space:nowrap}
  .hero-panel .btn{background:var(--blue);padding:10px 22px}

  .spotlight{height:400px;padding-top:48px}
  .spotlight .lead{text-align:center;font-size:15px;max-width:620px;margin:6px auto 0}
  .people{display:flex;justify-content:center;gap:20px;margin-top:20px}
  .person{text-align:center;width:152px}
  .person .photo{width:152px;height:152px;border-radius:50%;background:radial-gradient(circle at 50% 40%,#d8b49a,#8b6a58)}
  .person span{display:block;margin-top:12px;font-size:15px}

  .events{height:264px;margin:0 36px;background:linear-gradient(120deg,#dfe8ef,#b7c7d4 50%,#e7edf1);position:relative}
  .events-panel{position:absolute;left:116px;top:0;width:440px;height:264px;background:var(--blue-deep);color:#fff;padding:30px 56px}
  .events-panel h2{font-family:Montserrat,Arial,sans-serif;font-size:19px;text-align:center;letter-spacing:.5px;margin-bottom:22px}
  .event{display:flex;align-items:center;gap:12px;font-size:15px;margin-bottom:18px;white-space:nowrap}

  .tech{height:576px;padding-top:80px}
  .devices{display:flex;justify-content:center;gap:24px;margin-top:20px}
  .device{width:208px;text-align:center}
  .device .photo{width:208px;height:208px;border-radius:50%;background:radial-gradient(circle,#f4f4f4 40%,#e4e6e8)}
  .device p{font-size:15px;margin:16px 0 12px;height:46px;line-height:1.5}
  .tech .more{text-align:center;margin-top:24px}

  .pediatric{height:424px;padding-top:32px}
  .pediatric .sub{text-align:center;font-size:15px;margin-top:4px;line-height:22px}
  .ped-body{display:flex;justify-content:space-between;padding:0 44px 0 36px;margin-top:38px}
  .ped-body strong{display:block;font-size:14px;width:330px;margin-bottom:10px}
  .checklist{list-style:none}
  .checklist li{display:flex;align-items:flex-start;gap:10px;font-size:14px;margin-bottom:9px;width:320px}
  .checklist svg{flex:none;margin-top:3px}
  .ped-body .photo{width:272px;height:272px;border-radius:50%;background:radial-gradient(circle at 50% 45%,#f1d3c2,#b77a8f 75%);flex:none}

  .news{margin:24px 36px 0;height:480px;background:var(--sky-wash);padding:30px 32px}
  .news .sub{text-align:center;color:var(--blue);font-weight:600;font-size:15px;margin:4px 0 24px}
  .news-cols{display:flex;gap:28px}
  .news-cols > ul{flex:1}
  .news-cols .checklist li{width:auto;font-size:14px;margin-bottom:14px}

  .listen{height:328px;padding-top:24px}
  .listen-body{display:flex;gap:32px;padding:0 36px;margin-top:16px;align-items:center}
  .listen-body .photo{width:248px;height:240px;border-radius:50%;background:radial-gradient(circle at 50% 45%,#c7a38c,#6a4c3e 70%);flex:none}
  .listen-body h3{font-family:Montserrat,Arial,sans-serif;font-size:17px;color:var(--blue-deep);text-transform:uppercase;margin-bottom:8px}
  .listen-body p{font-size:14px;margin-bottom:18px}

  .note{height:360px;padding-top:56px;text-align:center}
  .avatar{width:80px;height:80px;border-radius:50%;margin:12px auto 8px;background:radial-gradient(circle at 50% 45%,#d9b8a4,#5a3d35 75%)}
  .doctor-name{font-weight:700;font-size:14px;line-height:20px}
  .doctor-role{font-size:13px;line-height:20px;color:var(--blue)}
  .note-box{margin:20px 36px 0;height:96px;background:var(--sky-wash);border:1px solid #cfe7f3;padding:14px 22px;text-align:left;font-size:13.5px;line-height:1.5}
  .note-box a{color:var(--blue-deep);font-weight:700;text-decoration:none}

  .social{height:152px;padding-top:64px;text-align:center}
  .social p{font-size:14px;margin-bottom:10px}
  .social-row{display:flex;justify-content:center;gap:12px}
  .social-row span{width:32px;height:32px;border-radius:50%;background:var(--blue-deep)}

  .contact-bar{margin:8px 36px 0;height:64px;border-top:1px solid var(--rule);border-bottom:1px solid var(--rule);background:#f6f8fa;display:flex;align-items:center;justify-content:space-around;font-size:13px;line-height:1.4}
  .contact-bar div{display:flex;align-items:center;gap:10px}
  .legal{text-align:center;font-size:13px;color:var(--ink-soft);margin-top:28px;line-height:1.8}
  .legal a{color:var(--link);text-decoration:underline}
</style>
</head>
<body>
  <p class="preheader">Is this email not displaying correctly?<br><a href="#">View it in your browser.</a></p>

  <main class="newsletter">
    <header class="masthead">
      <div class="brand"><span class="brand-dot"></span>Pinecrest Audiology</div>
      <div class="masthead-phone">
        <span class="icon-circle"><svg width="14" height="14" viewBox="0 0 24 24"><path fill="#fff" d="M6.6 10.8a15 15 0 0 0 6.6 6.6l2.2-2.2c.3-.3.7-.4 1-.2 1.1.4 2.3.6 3.6.6.6 0 1 .4 1 1V20c0 .6-.4 1-1 1A17 17 0 0 1 3 4c0-.6.4-1 1-1h3.5c.6 0 1 .4 1 1 0 1.3.2 2.5.6 3.6.1.3 0 .7-.2 1z"/></svg></span>
        Phone: (555) 014-2290
      </div>
    </header>

    <section class="hero" role="img" aria-label="Photo of the brick clinic building with its storefront sign">
      <div class="hero-panel">
        <h1>Identify. Equip. Inspire.</h1>
        <a class="btn" href="#">Visit Our Website</a>
      </div>
    </section>

    <section class="spotlight">
      <h2 class="section-title">Patient Spotlight</h2>
      <p class="lead">Pinecrest Audiology exists to provide exceptional hearing healthcare for patients of all ages. Our goal is to successfully bridge the gap between diagnosis and treatment for those with hearing loss.</p>
      <div class="people">
        <div class="person"><div class="photo" role="img" aria-label="Portrait of a child patient"></div><span>Child</span></div>
        <div class="person"><div class="photo" role="img" aria-label="Portrait of a young patient"></div><span>Young</span></div>
        <div class="person"><div class="photo" role="img" aria-label="Portrait of an adult patient"></div><span>Adult</span></div>
        <div class="person"><div class="photo" role="img" aria-label="Portrait of a senior patient"></div><span>Senior</span></div>
      </div>
    </section>

    <section class="events" role="img" aria-label="Background photo of a desk with stethoscope and clinic paperwork">
      <div class="events-panel">
        <h2>UPCOMING EVENTS</h2>
        <div class="event"><svg width="18" height="18" viewBox="0 0 24 24"><circle cx="12" cy="12" r="9" fill="none" stroke="#fff" stroke-width="2"/><path d="M12 7v5l3 2" stroke="#fff" stroke-width="2" fill="none"/></svg>12.02.2016 – Free Checkup</div>
        <div class="event"><svg width="18" height="18" viewBox="0 0 24 24"><circle cx="12" cy="12" r="9" fill="none" stroke="#fff" stroke-width="2"/><path d="M12 7v5l3 2" stroke="#fff" stroke-width="2" fill="none"/></svg>12.03.2016 – Doctor Q&amp;A Evening</div>
        <div class="event"><svg width="18" height="18" viewBox="0 0 24 24"><circle cx="12" cy="12" r="9" fill="none" stroke="#fff" stroke-width="2"/><path d="M12 7v5l3 2" stroke="#fff" stroke-width="2" fill="none"/></svg>12.03.2016 – Patients/Doctor Gathering</div>
      </div>
    </section>

    <section class="tech">
      <h2 class="section-title">Technology Update</h2>
      <div class="devices">
        <div class="device"><div class="photo" role="img" aria-label="Product photo of two hearing aids"></div><p>Made for Smartphone<br>Hearing Aids</p><span class="btn-outline">Details Here ›</span></div>
        <div class="device"><div class="photo" role="img" aria-label="Product photo of rechargeable hearing aids in a charger"></div><p>Rechargeable<br>Hearing Aids</p><span class="btn-outline">Details Here ›</span></div>
        <div class="device"><div class="photo" role="img" aria-label="Product photo of a TV streaming device"></div><p>TV and Music<br>Streaming</p><span class="btn-outline">Details Here ›</span></div>
      </div>
      <div class="more"><a class="btn" href="#">More Details Here</a></div>
    </section>

    <section class="pediatric">
      <h2 class="section-title">Pediatric Corner</h2>
      <p class="sub">Our goal is to maximize every child's hearing potential!</p>
      <div class="ped-body">
        <div>
          <strong>Common reasons to schedule a hearing evaluation for your child include:</strong>
          <ul class="checklist">
            <li><svg width="14" height="14" viewBox="0 0 14 14"><circle cx="7" cy="7" r="6.5" fill="none" stroke="#7a8088"/><path d="M4 7l2 2 4-4" stroke="#7a8088" fill="none" stroke-width="1.4"/></svg>speech delay</li>
            <li><svg width="14" height="14" viewBox="0 0 14 14"><circle cx="7" cy="7" r="6.5" fill="none" stroke="#7a8088"/><path d="M4 7l2 2 4-4" stroke="#7a8088" fill="none" stroke-width="1.4"/></svg>frequent or recurrent ear infections</li>
            <li><svg width="14" height="14" viewBox="0 0 14 14"><circle cx="7" cy="7" r="6.5" fill="none" stroke="#7a8088"/><path d="M4 7l2 2 4-4" stroke="#7a8088" fill="none" stroke-width="1.4"/></svg>known risk factors for hearing loss</li>
            <li><svg width="14" height="14" viewBox="0 0 14 14"><circle cx="7" cy="7" r="6.5" fill="none" stroke="#7a8088"/><path d="M4 7l2 2 4-4" stroke="#7a8088" fill="none" stroke-width="1.4"/></svg>family history of hearing loss</li>
            <li><svg width="14" height="14" viewBox="0 0 14 14"><circle cx="7" cy="7" r="6.5" fill="none" stroke="#7a8088"/><path d="M4 7l2 2 4-4" stroke="#7a8088" fill="none" stroke-width="1.4"/></svg>diagnosis of a learning disability or other learning disorder</li>
            <li><svg width="14" height="14" viewBox="0 0 14 14"><circle cx="7" cy="7" r="6.5" fill="none" stroke="#7a8088"/><path d="M4 7l2 2 4-4" stroke="#7a8088" fill="none" stroke-width="1.4"/></svg>concern about attention</li>
          </ul>
        </div>
        <div class="photo" role="img" aria-label="Photo of a smiling toddler in a pink top"></div>
      </div>
    </section>

    <section class="news">
      <h2 class="section-title">Exciting News</h2>
      <p class="sub">If you pursue a trial with amplification then you can enjoy...</p>
      <div class="news-cols">
        <ul class="checklist">
          <li><svg width="14" height="14" viewBox="0 0 14 14"><circle cx="7" cy="7" r="7" fill="#0892cd"/><path d="M4 7l2 2 4-4" stroke="#fff" fill="none" stroke-width="1.5"/></svg>Custom hearing solution selected to meet your individual listening, aesthetic, and financial needs</li>
          <li><svg width="14" height="14" viewBox="0 0 14 14"><circle cx="7" cy="7" r="7" fill="#0892cd"/><path d="M4 7l2 2 4-4" stroke="#fff" fill="none" stroke-width="1.5"/></svg>Expert fitting, thorough orientation and research-based verification of hearing aid output</li>
          <li><svg width="14" height="14" viewBox="0 0 14 14"><circle cx="7" cy="7" r="7" fill="#0892cd"/><path d="M4 7l2 2 4-4" stroke="#fff" fill="none" stroke-width="1.5"/></svg>3-year manufacturer's warranty / 3-year Loss &amp; Damage policy</li>
          <li><svg width="14" height="14" viewBox="0 0 14 14"><circle cx="7" cy="7" r="7" fill="#0892cd"/><path d="M4 7l2 2 4-4" stroke="#fff" fill="none" stroke-width="1.5"/></svg>Competitive pricing and special financing available with approved credit</li>
        </ul>
        <ul class="checklist">
          <li><svg width="14" height="14" viewBox="0 0 14 14"><circle cx="7" cy="7" r="7" fill="#0892cd"/><path d="M4 7l2 2 4-4" stroke="#fff" fill="none" stroke-width="1.5"/></svg>45-day trial period</li>
          <li><svg width="14" height="14" viewBox="0 0 14 14"><circle cx="7" cy="7" r="7" fill="#0892cd"/><path d="M4 7l2 2 4-4" stroke="#fff" fill="none" stroke-width="1.5"/></svg>1-year supply of batteries for those hearing aids utilizing disposable batteries</li>
          <li><svg width="14" height="14" viewBox="0 0 14 14"><circle cx="7" cy="7" r="7" fill="#0892cd"/><path d="M4 7l2 2 4-4" stroke="#fff" fill="none" stroke-width="1.5"/></svg>Care and maintenance supplies</li>
          <li><svg width="14" height="14" viewBox="0 0 14 14"><circle cx="7" cy="7" r="7" fill="#0892cd"/><path d="M4 7l2 2 4-4" stroke="#fff" fill="none" stroke-width="1.5"/></svg>Most devices fit with 3-year hearing aid care package that covers all follow-up hearing aid programming visits and regular cleanings at Pinecrest Audiology</li>
        </ul>
      </div>
    </section>

    <section class="listen">
      <h2 class="section-title">Learn to Listen</h2>
      <div class="listen-body">
        <div class="photo" role="img" aria-label="Photo of an audiologist fitting a hearing aid on a patient"></div>
        <div>
          <h3>Hearing Care for All Ages</h3>
          <p>Pinecrest Audiology exists to provide exceptional hearing healthcare for patients of all ages. Our goal is to successfully bridge the gap between diagnosis and treatment for those with hearing loss.</p>
          <a class="btn" href="#">See Details Here</a>
        </div>
      </div>
    </section>

    <section class="note">
      <h2 class="section-title">A Note From Dr. Farrow</h2>
      <div class="avatar" role="img" aria-label="Portrait photo of Dr. Farrow"></div>
      <p class="doctor-name">Dana Farrow, AuD, CCC-A</p>
      <p class="doctor-role">Doctor of Audiology</p>
      <div class="note-box">Dr. Farrow opened Pinecrest Audiology in 2015 after realizing the void of care that existed within her own community for those younger listeners affected by hearing loss. The past two years she has worked tirelessly... <a href="#">Read More»</a></div>
    </section>

    <section class="social">
      <p>Connected with us by</p>
      <div class="social-row"><span></span><span></span></div>
    </section>

    <footer>
      <div class="contact-bar">
        <div><span class="icon-circle"><svg width="14" height="14" viewBox="0 0 24 24"><path fill="#fff" d="M6.6 10.8a15 15 0 0 0 6.6 6.6l2.2-2.2c.3-.3.7-.4 1-.2 1.1.4 2.3.6 3.6.6.6 0 1 .4 1 1V20c0 .6-.4 1-1 1A17 17 0 0 1 3 4c0-.6.4-1 1-1h3.5c.6 0 1 .4 1 1 0 1.3.2 2.5.6 3.6.1.3 0 .7-.2 1z"/></svg></span>Call Us: (555) 014-2290</div>
        <div><span class="icon-circle"><svg width="14" height="14" viewBox="0 0 24 24"><path fill="#fff" d="M12 2a7 7 0 0 0-7 7c0 5 7 13 7 13s7-8 7-13a7 7 0 0 0-7-7zm0 9.5A2.5 2.5 0 1 1 12 6.5a2.5 2.5 0 0 1 0 5z"/></svg></span><span>Place: 118 Birch Hollow Rd, Suite 210<br>Ashford, SC 29000</span></div>
      </div>
      <p class="legal">You're receiving this newsletter because you signed up on our site<br><a href="#">View it in your browser</a> | <a href="#">Unsubscribe instantly</a></p>
    </footer>
  </main>
</body>
</html>
```